Rack card for a integrative medical practice

Need an eye-catching rack card with our logo with content as provided. We have a membership based holistic medical practice which incorporates western and holistic medicine. We would like to focus on wellness and healthy lifestyle. See uploaded files for what is included in the membership. Would like 2 page rack card color on both sides. Logo must be on the front.

Target Market(s)

People looking for alternative medicine, healthy lifestyle.

Industry/Entity Type

Health and Wellness

Colors
00AB8E
00BBA5
67D7C9
C6EFE9
E9F9F6

Requirements
Must have
• Must spark interest at first sight. Clear message.
Nice to have
• Warm, bright and positive vibe. Organic, neutral and earthy colors.
Should not have
• Traditional medical practice vibe (cold, formal, industrial). No PINK except the logo.

```html
<!DOCTYPE html>
<html lang="en">
<head>
<meta charset="utf-8">
<title>Fernleaf Health &amp; Wellness — Rack Card</title>
<link href="https://fonts.googleapis.com/css2?family=Bodoni+Moda:wght@500;600;700&family=Montserrat:wght@400;500&display=swap" rel="stylesheet">
<style>
  :root {
    --backdrop: #5e5e5e;
    --forest: #0a3028;
    --cream: #f5ede1;
    --paper: #ffffff;
    --accent: #e0197a;
    --gold: #f0cf9f;
    --ink: #1c1c1c;
    --rule: #2c4a43;
  }
  * { margin: 0; padding: 0; box-sizing: border-box; }
  html, body { width: 1200px; height: 1200px; overflow: hidden; }
  body { background: var(--backdrop); position: relative; font-family: "Montserrat", sans-serif; }

  .card { position: absolute; top: 135px; width: 412px; height: 928px; overflow: hidden; background: var(--paper); }
  .card--front { left: 126px; }
  .card--back { left: 658px; }
  .card__shapes { position: absolute; inset: 0; width: 100%; height: 100%; }

  .hero-photo {
    position: absolute; left: 0; top: 0; width: 412px; height: 400px;
    background: linear-gradient(120deg, #dfe3e2 0%, #a7ad9f 25%, #6d5a4d 50%, #4a3b33 75%, #3a2e29 100%);
  }

  .brand { position: absolute; left: 0; width: 100%; display: flex; align-items: center; justify-content: center; gap: 12px; }
  .brand__dot { width: 22px; height: 22px; border-radius: 50%; background: var(--forest); flex: none; }
  .brand__name { font-family: "Bodoni Moda", serif; font-weight: 600; font-size: 40px; line-height: 1; color: var(--forest); }
  .card--front .brand { top: 452px; }
  .card--back .brand { top: 812px; }

  .front-title { position: absolute; top: 555px; left: 0; width: 100%; text-align: center;
    font-family: "Bodoni Moda", serif; font-weight: 600; font-size: 41px; line-height: 48px; color: var(--forest); }
  .accent-rule { position: absolute; left: 50%; width: 40px; height: 2px; margin-left: -20px; background: var(--accent); }
  .card--front .accent-rule { top: 653px; }
  .card--back .accent-rule { top: 231px; }
  .front-tagline { position: absolute; top: 670px; left: 0; width: 100%; text-align: center; white-space: nowrap;
    font-size: 14.2px; line-height: 20.5px; letter-spacing: 0.4px; color: var(--ink); text-transform: uppercase; }

  .address { position: absolute; top: 818px; left: 0; width: 100%; text-align: center;
    font-family: "Bodoni Moda", serif; font-weight: 600; font-size: 16.5px; line-height: 21px; color: var(--ink); }
  .address svg { display: block; margin: 0 auto 8px; }

  .back-title { position: absolute; top: 136px; left: 0; width: 100%; text-align: center;
    font-family: "Bodoni Moda", serif; font-weight: 600; font-size: 25px; line-height: 28px; color: var(--paper); }

  .benefits { position: absolute; top: 252px; left: 50px; width: 312px; list-style: none; }
  .benefits li { position: relative; text-align: center; white-space: nowrap; font-size: 14px; line-height: 17px;
    letter-spacing: 0.5px; color: var(--ink); padding: 11px 0 12px; }
  .benefits li:first-child { padding-top: 0; }
  .benefits li::after { content: ""; position: absolute; left: 34px; right: 34px; bottom: 0; height: 1px; background: var(--rule); }
  .benefits li:last-child::after { display: none; }
</style>
</head>
<body>

<section class="card card--front">
  <div class="hero-photo" role="img" aria-label="Photo of a smiling woman outdoors with eyes closed, beside a lake and tree trunk"></div>
  <svg class="card__shapes" viewBox="0 0 412 928" aria-hidden="true">
    <path fill="#f5ede1" d="M0 376 L20 368 L34 372 L50 362 L70 364 L86 350 L104 354 L118 342 L140 346 L156 336 L172 340 L188 326 L210 332 L226 320 L246 328 L262 318 L282 322 L300 310 L322 316 L340 306 L360 312 L378 300 L396 306 L412 296 L412 928 L0 928 Z"/>
    <path fill="#ffffff" d="M0 782 L18 774 L40 776 L64 768 L92 770 L118 764 L148 766 L170 760 L196 764 L222 762 L250 768 L274 772 L300 780 L324 790 L346 806 L364 822 L380 838 L396 852 L412 862 L412 928 L0 928 Z"/>
  </svg>
  <div class="brand">
    <div class="brand__dot"></div>
    <div class="brand__name">Fernleaf</div>
  </div>
  <h1 class="front-title">Fernleaf Health &amp;<br>Wellness</h1>
  <div class="accent-rule"></div>
  <p class="front-tagline">A direct primary care practice<br>focused on a more holistic &amp; personal<br>approach to medicine.</p>
  <div class="address">
    <svg width="13" height="16" viewBox="0 0 13 16"><path fill="#0a3028" d="M6.5 0C2.9 0 0 2.8 0 6.3 0 10.5 6.5 16 6.5 16S13 10.5 13 6.3C13 2.8 10.1 0 6.5 0Zm0 8.6a2.3 2.3 0 1 1 0-4.6 2.3 2.3 0 0 1 0 4.6Z"/></svg>
    1420 Willow Bend Rd., STE 2B<br>Riverton
  </div>
</section>

<section class="card card--back">
  <svg class="card__shapes" viewBox="0 0 412 928" aria-hidden="true">
    <path fill="#0a3028" d="M0 0 L412 0 L412 204 L396 206 L382 212 L360 214 L330 218 L300 219 L270 218 L240 216 L200 214 L170 212 L140 210 L110 208 L80 206 L50 204 L30 206 L10 208 L0 210 Z"/>
    <line x1="25" y1="235" x2="25" y2="697" stroke="#f0cf9f" stroke-width="1"/>
    <line x1="31" y1="235" x2="31" y2="697" stroke="#f0cf9f" stroke-width="1"/>
    <line x1="380" y1="235" x2="380" y2="697" stroke="#f0cf9f" stroke-width="1"/>
    <line x1="386" y1="235" x2="386" y2="697" stroke="#f0cf9f" stroke-width="1"/>
    <path fill="#f5ede1" d="M0 760 L24 752 L50 748 L80 744 L110 740 L140 738 L170 736 L200 732 L230 728 L260 730 L290 726 L320 730 L350 734 L380 730 L400 736 L412 734 L412 928 L0 928 Z"/>
  </svg>
  <h2 class="back-title">WHAT'S INCLUDED<br>IN YOUR MEMBERSHIP</h2>
  <div class="accent-rule"></div>
  <ul class="benefits">
    <li>Unlimited office visits with no copay</li>
    <li>Direct communication with your<br>doctor</li>
    <li>Discounted labs, imaging and<br>medications</li>
    <li>Free initial acupuncture session<br>($250value).</li>
    <li>2 body composition tests per year<br>($100 value)</li>
    <li>Discounts for supplements and health<br>products in the clinic</li>
    <li>Discounts for iv vitamin infusion<br>therapy</li>
    <li>Personalized nutrition plan after<br>advanced testing such as gut<br>microbiome, hormonal, metabolism<br>test, etc.</li>
  </ul>
  <div class="brand">
    <div class="brand__dot"></div>
    <div class="brand__name">Fernleaf</div>
  </div>
</section>

</body>
</html>
```